Fun, Clean Business Card For Family Focused Travel Agency

I need a business card using specific colors and fonts as in the uploaded files. Ideally, I would like a large image of the logo on the back and all the contact info on the front. Maybe the stars/dots somewhere in a flowy form.

I do want it the contact information to be clear and easy to read. I don't want it to look too busy. Maybe even a bit minimalist.

I plan or ordering the ROUNDED CORNER business cards from Cardmerix, so please consider that in your design.

Target Market(s)

Families with children, couples, groups of friends

Contact Information for Business Card

Delia Marsh, Owner
Delia@WillowTrekTrips.example
Cell Phone Number 555-214-3967
Office Phone Number 555-862-1504
Specializing in Kelvaro destinations, Pemberly Coast Park Resort, Cruises and All-Inclusive Vacations.

Nice but not required:
www.WillowTrekTrips.example
Chatterly, Snapvista, Quipwing icons with username: WillowTrekTrips

Font styles to use
Sans Serif

Requirements
Must have
• Please try to use the colors from the logo as much as possible. I understand lighter shades/colors may be needed for some things.
Should not have
• NO SERIF FONTS. That is really the only thing I do not want at all

```html
<!DOCTYPE html>
<html lang="en">
<head>
<meta charset="utf-8">
<title>WillowTrek Trips Business Cards</title>
<link rel="stylesheet" href="https://fonts.googleapis.com/css2?family=Open+Sans:wght@400;600;700&display=swap">
<style>
  :root {
    --backdrop: #2e2f31;
    --card: #ffffff;
    --ink: #1b2236;
    --text: #2a2a2a;
    --teal: #1fb18f;
    --orange: #f07f22;
    --ghost-grey: #c9c8cf;
    --ghost-teal: #cdeee4;
    --ghost-peach: #fbe3cf;
  }
  * { margin: 0; padding: 0; box-sizing: border-box; }
  html, body {
    width: 1200px; height: 900px; overflow: hidden;
    background: var(--backdrop);
    font-family: "Open Sans", Arial, sans-serif;
  }
  .stage { position: relative; width: 1200px; height: 900px; }
  .card {
    position: absolute;
    width: 600px; height: 340px;
    background: var(--card);
    border-radius: 28px;
    overflow: hidden;
    box-shadow: 0 18px 40px rgba(0,0,0,0.45);
  }
  .card-front { left: 70px; top: 60px; }
  .card-back { left: 530px; top: 490px; }
  .edge-band {
    position: absolute; left: 0; right: 0; bottom: 0; height: 12px;
    display: flex;
  }
  .edge-band .band-orange { flex: 0 0 57%; background: var(--orange); }
  .edge-band .band-teal { flex: 1; background: var(--teal); }

  .brand {
    display: flex; align-items: center; gap: 14px;
    color: var(--ink); font-weight: 700; white-space: nowrap;
  }
  .brand-dot { border-radius: 50%; background: var(--teal); flex: none; }

  .card-front .brand {
    position: absolute; left: 0; right: 0; top: 130px;
    justify-content: center; font-size: 50px; letter-spacing: -0.5px;
  }
  .card-front .brand-dot { width: 34px; height: 34px; }

  .card-back .brand {
    position: absolute; left: 44px; top: 78px;
    font-size: 34px; letter-spacing: -0.3px;
  }
  .card-back .brand-dot { width: 24px; height: 24px; }

  .mark-ghost {
    position: absolute; right: 18px; top: 36px;
    width: 180px; height: 262px;
    border-radius: 46% 46% 30% 30%;
    background: linear-gradient(160deg, var(--ghost-grey) 0%, var(--ghost-teal) 55%, var(--ghost-peach) 100%);
    opacity: 0.75;
  }

  .contact {
    position: absolute; left: 30px; top: 168px; width: 370px;
    text-align: center; color: var(--text);
    font-size: 17px; line-height: 1.45;
  }
  .contact .holder { font-weight: 700; color: var(--ink); }
</style>
</head>
<body>
<main class="stage">
  <section class="card card-front">
    <div class="brand"><span class="brand-dot"></span><span>WillowTrek Trips</span></div>
    <div class="edge-band"><span class="band-orange"></span><span class="band-teal"></span></div>
  </section>

  <section class="card card-back">
    <div class="mark-ghost" role="img" aria-label="Large faint brand symbol decoration with scattered stars and dots"></div>
    <div class="brand"><span class="brand-dot"></span><span>WillowTrek Trips</span></div>
    <div class="contact">
      <p class="holder">Delia Marsh | Owner</p>
      <p>Email : Delia@WillowTrekTrips.example</p>
      <p>Cell Phone : 555-214-3967</p>
      <p>Office Phone : 555-862-1504</p>
    </div>
    <div class="edge-band"><span class="band-orange"></span><span class="band-teal"></span></div>
  </section>
</main>
</body>
</html>
```